Prospective Client Introduction Brochure/Packet

We need a "Welcome Packet" for a Private Wealth Management Firm to give to prospective clients. It will need to be print ready as it is something we will hand to them or mail to them in a hard copy form. Might even need help designing a few extra pieces. Want a professional piece that share with people, who our firm is, what we do and how we help clients, We will need to provide pics and such but want to narrow down a "look"

Target Market(s)

Business owners and retiree's/ retired individuals

Industry/Entity Type

Financial Services

Font styles to use
Serif
Sans Serif

Colors
0054AA
0677BA
7BADD7
CADEEF
E8F1F8

Requirements
Must have
• Include the KTM logo as best as possible be easy to read
Nice to have
• Flow Chart's of the journey,
Should not have
• Cartoon like images

```html
<!DOCTYPE html>
<html lang="en">
<head>
<meta charset="utf-8">
<title>Family Wealth Planning &amp; Client Services</title>
<link rel="stylesheet" href="https://fonts.googleapis.com/css2?family=Abril+Fatface&family=Jost:wght@300;400&display=swap">
<style>
:root{
  --navy:#0a2a66;
  --ink:#1a1a1a;
  --ghost:#e2e2e2;
  --bg:#ffffff;
}
*{margin:0;padding:0;box-sizing:border-box}
html,body{width:849px;height:1200px;overflow:hidden;background:var(--bg)}
.page{position:relative;width:849px;height:1200px}
.section-number{position:absolute;font-family:"Jost",sans-serif;font-weight:400;color:var(--ghost);font-size:300px;line-height:1;letter-spacing:-6px;z-index:0}
.section-title{position:absolute;font-family:"Abril Fatface",serif;color:var(--navy);font-size:42px;line-height:45px;z-index:1}
.service-list{position:absolute;list-style:none;font-family:"Jost",sans-serif;font-weight:300;font-size:14.6px;line-height:22.8px;color:var(--ink);text-align:justify;z-index:1}
.service-list li{position:relative;padding-left:15px}
.service-list li::before{content:"•";position:absolute;left:0;font-weight:400}
.photo{position:absolute;border-radius:16px}
.photo-beach{left:462px;top:64px;width:351px;height:302px;background:linear-gradient(180deg,#8fc4ef 0%,#bfe0f5 38%,#35b4c8 55%,#9fd8d8 75%,#e6d3b6 100%)}
.photo-laptop{left:36px;top:449px;width:350px;height:301px;background:linear-gradient(135deg,#5a3a30 0%,#d9d6d0 35%,#f1f0ec 70%,#e4e2de 100%)}
</style>
</head>
<body>
<main class="page">
  <section class="service family-planning">
    <div class="section-number" style="left:108px;top:60px">04</div>
    <h2 class="section-title" style="left:69px;top:68px">Family Wealth<br>Planning</h2>
    <ul class="service-list" style="left:71px;top:176px;width:348px">
      <li>Analysis of your current estate plan and concerns</li>
      <li>Complimentary consultation with your attorney</li>
      <li>Assistance in transferring assets to your Living Trust or other trusts</li>
      <li>Analysis of the beneficiaries of your IRAs and how to establish an Inherited IRA</li>
      <li>Providing guidance with the appropriate and necessary steps in the event of the death of a loved one</li>
    </ul>
    <div class="photo photo-beach" role="img" aria-label="Father holding a young daughter's hand walking into the sea on a sunny beach"></div>
  </section>

  <section class="service client-services">
    <div class="photo photo-laptop" role="img" aria-label="Person working on a laptop showing financial charts beside a phone and glasses"></div>
    <div class="section-number" style="left:483px;top:505px">05</div>
    <h2 class="section-title" style="left:445px;top:436px">Client Services &amp;<br>Communications</h2>
    <ul class="service-list" style="left:428px;top:534px;width:378px">
      <li>Access to our customized online wealth management portal</li>
      <li>Quarterly “market watch” letters detailing our firm’s research, analysis and view of the current state of the investment markets</li>
      <li>Economic and educational seminars held throughout the year (guests welcome)</li>
      <li>Special client appreciation events (where you may bring up to 2 guests)</li>
      <li>Annual meetings to review and evaluate your investment performance, portfolio allocation, and update your financial plan.</li>
    </ul>
  </section>
</main>
</body>
</html>
```